Elder abuse Infographic Poster for doctor surgeries

I am looking for someone to redesign, or clean up an infographic poster that we have drafted to raise awareness for Elder abuse. The colour for elder abuse is deep dark purple, and we would like it to be high resolution so it can be printed A3 size and placed in Doctor surgeries. The poster will be used by a not-for-profit in Australia. We are looking to use pictures, rather than heavy text blocks, following the Infographic poster style (I have included a couple of infographic posters for inspiration).
Reason: Providing extra time for more designs :)
Target Market(s)
Older people, 60+
Industry/Entity Type
Doctor
Requirements
Nice to have
- NOTE: You do not need to use the banner etc I have attached, its just an idea for the colours we use etc.
Should not have
- Images of frail older people, pastel colourings, or anything typically associated with frail aged.

```html
<!DOCTYPE html>
<html lang="en">
<head>
<meta charset="utf-8">
<title>Elder Abuse Awareness Poster</title>
<link href="https://fonts.googleapis.com/css2?family=Anton&family=Open+Sans:wght@400;600&display=swap" rel="stylesheet">
<style>
  :root {
    --purple-deep: #1c0748;
    --purple: #2e0c6e;
    --purple-glow: rgba(90, 40, 170, 0.45);
    --white: #ffffff;
    --sky: #bff3fa;
    --magenta: #d52ee0;
    --card-aqua: #b4e0ea;
    --card-purple: #b214e2;
    --card-blue: #2a6de6;
    --ink: #14083a;
  }
  * { margin: 0; padding: 0; box-sizing: border-box; }
  html, body { width: 849px; height: 1200px; overflow: hidden; background: var(--purple-deep); }
  .poster {
    position: relative;
    width: 849px;
    height: 1200px;
    overflow: hidden;
    font-family: "Anton", Impact, sans-serif;
    color: var(--white);
  }
  .backdrop-photo {
    position: absolute; inset: 0;
    background:
      radial-gradient(ellipse 420px 360px at 420px 260px, var(--purple-glow), transparent 70%),
      radial-gradient(ellipse 360px 320px at 160px 620px, rgba(80, 35, 160, 0.4), transparent 70%),
      radial-gradient(ellipse 300px 300px at 650px 560px, rgba(75, 30, 150, 0.35), transparent 70%),
      linear-gradient(180deg, var(--purple) 0%, var(--purple-deep) 100%);
  }
  .brand-pill {
    position: absolute; left: 173px; top: 45px;
    width: 493px; height: 110px;
    background: var(--white);
    border-radius: 55px;
    display: flex; align-items: center; justify-content: center;
  }
  .brand-name {
    font-size: 52px;
    color: var(--magenta);
    letter-spacing: 1px;
  }
  .headline { position: absolute; left: 0; width: 849px; text-align: center; white-space: nowrap; }
  .headline-lead { top: 286px; font-size: 29px; color: var(--sky); letter-spacing: 0.6px; }
  .headline-main { top: 316px; font-size: 146px; line-height: 1.1; letter-spacing: 6px; padding-left: 6px; }
  .headline-stat { top: 460px; font-size: 35px; color: var(--magenta); letter-spacing: 1.5px; }
  .info-card {
    position: absolute; top: 731px;
    width: 266px; height: 286px;
    padding: 20px 22px 0 30px;
  }
  .info-card::before {
    content: ""; position: absolute; top: -12px;
    left: var(--tab-left);
    width: 101px; height: 22px;
    background: var(--white); border-radius: 11px;
  }
  .card-types { left: 8px; background: var(--card-aqua); --tab-left: 79px; }
  .card-prevention { left: 290px; background: var(--card-purple); --tab-left: 82px; }
  .card-stopping { left: 576px; background: var(--card-blue); --tab-left: 85px; }
  .card-title { font-size: 27px; font-weight: 400; letter-spacing: 0.5px; line-height: 1.2; }
  .card-types .card-title { color: var(--ink); }
  .card-icon {
    position: absolute; top: 20px; right: 12px;
    width: 30px; height: 30px;
  }
  .card-body {
    margin-top: 22px;
    padding-left: 4px;
    font-family: "Open Sans", Arial, sans-serif;
    font-size: 15.5px; line-height: 21.8px;
  }
  .card-types .card-body { color: var(--ink); }
  .helpline { position: absolute; left: 0; width: 849px; text-align: center; white-space: nowrap; }
  .helpline-label { top: 1062px; font-size: 23px; letter-spacing: 0.8px; }
  .helpline-number { top: 1086px; font-size: 82px; line-height: 1.1; letter-spacing: 6px; padding-left: 6px; }
</style>
</head>
<body>
<main class="poster">
  <div class="backdrop-photo" role="img" aria-label="Faint deep purple photograph of smiling older people filling the poster background"></div>

  <header class="brand-pill">
    <span class="brand-name">Elderguard Inc.</span>
  </header>

  <p class="headline headline-lead">There is no excuse for</p>
  <h1 class="headline headline-main">Elder Abuse</h1>
  <p class="headline headline-stat">1 in 20 OLder people will experience elder abuse</p>

  <section class="info-card card-types">
    <h2 class="card-title">Types of Abuse</h2>
    <svg class="card-icon" viewBox="0 0 30 30" aria-hidden="true">
      <circle cx="15" cy="15" r="14" fill="#14083a"/>
      <rect x="13.2" y="6.5" width="3.6" height="11" rx="1.8" fill="#b4e0ea"/>
      <circle cx="15" cy="22" r="2.1" fill="#b4e0ea"/>
    </svg>
    <p class="card-body">Abuse can be physical, emotional, financial, sexual or neglect. It is often caused by someone the person trusts, such as family or a carer.</p>
  </section>

  <section class="info-card card-prevention">
    <h2 class="card-title">Prevention</h2>
    <svg class="card-icon" viewBox="0 0 30 30" aria-hidden="true">
      <circle cx="15" cy="15" r="14" fill="#ffffff"/>
      <path d="M8.5 15.5 L13 20 L21.5 10.5" fill="none" stroke="#b214e2" stroke-width="3.2" stroke-linecap="round" stroke-linejoin="round"/>
    </svg>
    <p class="card-body">Stay connected with friends and community. Plan ahead with a trusted enduring power of attorney. Keep your money and documents safe.</p>
  </section>

  <section class="info-card card-stopping">
    <h2 class="card-title">Stopping Abuse</h2>
    <svg class="card-icon" viewBox="0 0 30 30" aria-hidden="true">
      <circle cx="15" cy="15" r="14" fill="#ffffff"/>
      <path d="M10.2 7.5 c1-.6 1.8-.3 2.3.6 l1.5 2.8 c.4.8.2 1.6-.5 2.1 l-1.2.9 c.9 2 2.3 3.5 4.2 4.5 l1-1.1 c.6-.6 1.4-.7 2.1-.3 l2.7 1.6 c.9.5 1.1 1.4.5 2.3 l-1 1.4 c-.8 1.1-2.2 1.5-3.5 1 c-4.6-1.8-8.1-5.4-9.7-10.1 c-.4-1.3 0-2.7 1.1-3.5 z" fill="#2a6de6"/>
    </svg>
    <p class="card-body">If you suspect abuse, talk to your doctor or call the helpline. Calls are free and confidential. In an emergency call 000.</p>
  </section>

  <p class="helpline helpline-label">Elder Abuse Helpline</p>
  <p class="helpline helpline-number">1300 555 014</p>
</main>
</body>
</html>
```